Varlo Building Pty Ltd need an Identity!

We need a logo design for a building company based in Sydney, Australia. In addition - Business Card Layout. The colour scheme is to be black and red and communicate a professional yet 'hands on' approach to building.

Target Market(s)

Architects, Home Owners, Developers

Industry/Entity Type

Construction

Font styles to use
Serif
Sans Serif

Colors
ec1f27

Requirements
Must have
• Clear logo and professional direction.
Nice to have
• Use of initials as a possible logo
Should not have
• Graphics/pictures of houses, house roofs etc. Can be an abstracted form of a building.

```html
<!DOCTYPE html>
<html lang="en">
<head>
<meta charset="utf-8">
<title>Varlo Building Pty Ltd – Stationery</title>
<link href="https://fonts.googleapis.com/css2?family=Archivo:wght@700&family=Arimo:wght@700&display=swap" rel="stylesheet">
<style>
  :root {
    --red: #ff0000;
    --ink: #111111;
    --paper: #ffffff;
    --edge: #d6d6d6;
    --faint: #d2d2d2;
    --brick-dark: #5a2a2c;
    --brick-mid: #b03a3c;
    --brick-bright: #e8262a;
  }
  * { margin: 0; padding: 0; box-sizing: border-box; }
  html, body { width: 1200px; height: 1200px; overflow: hidden; background: var(--paper); }
  body { position: relative; font-family: "Arimo", Arial, sans-serif; }

  .letterhead {
    position: absolute; left: 48px; top: 40px; width: 791px; height: 1120px;
    border: 1px solid var(--edge); background: var(--paper); overflow: hidden;
  }
  .letterhead__mark {
    position: absolute; left: 62px; top: 130px;
    font-family: "Archivo", sans-serif; font-weight: 700; font-size: 40px; color: var(--ink);
  }
  .letterhead__name {
    position: absolute; left: 232px; top: 94px;
    font-family: "Archivo", sans-serif; font-weight: 700; font-size: 47px; color: var(--ink);
    letter-spacing: 0.2px; white-space: nowrap;
  }
  .letterhead__rule {
    position: absolute; left: 224px; top: 148px; width: 504px; height: 2px; background: var(--red);
  }
  .letterhead__contact {
    position: absolute; left: 234px; top: 153px;
    font-weight: 700; font-size: 15px; line-height: 19px; color: var(--red); white-space: nowrap;
  }
  .letterhead__watermark {
    position: absolute; left: 0; right: 0; top: 490px; text-align: center;
    font-family: "Archivo", sans-serif; font-weight: 700; font-size: 150px; color: var(--faint);
  }
  .skyline {
    position: absolute; left: 0; right: 0; bottom: 0;
    background: linear-gradient(100deg, var(--brick-dark), var(--brick-bright) 30%, var(--brick-mid) 55%, var(--brick-bright) 80%, var(--brick-dark));
  }
  .letterhead .skyline { height: 132px; }

  .card {
    position: absolute; left: 874px; top: 374px; width: 278px; height: 474px;
    border: 1px solid var(--edge); background: var(--paper); overflow: hidden;
  }
  .card .skyline { height: 56px; }
  .card__vertical {
    position: absolute; writing-mode: vertical-rl; transform: rotate(180deg); white-space: nowrap;
  }
  .card__name {
    left: 190px; top: 47px;
    font-family: "Archivo", sans-serif; font-weight: 700; font-size: 24px; color: var(--ink);
  }
  .card__rule {
    position: absolute; left: 218px; top: 44px; width: 2px; height: 300px; background: var(--red);
  }
  .card__contact {
    left: 221px; top: 96px; font-size: 7px; line-height: 10px; color: var(--red);
  }
  .card__mark {
    left: 186px; top: 318px;
    font-family: "Archivo", sans-serif; font-weight: 700; font-size: 22px; color: var(--ink);
  }
  .card__person { left: 46px; top: 228px; color: var(--red); }
  .card__person-name { font-size: 13px; font-weight: 700; }
  .card__person-role { font-size: 6px; font-weight: 700; }
</style>
</head>
<body>
  <section class="letterhead" aria-label="Letterhead">
    <div class="letterhead__mark">Varlo</div>
    <h1 class="letterhead__name">Varlo Building Pty Ltd</h1>
    <div class="letterhead__rule"></div>
    <p class="letterhead__contact">
      Address : xoxoxoxo, xoxo xoxoxo, xoxoxo - xoxoxo<br>
      Cell : 40404040 E-mail : hello@varlobuilding.com.au
    </p>
    <div class="letterhead__watermark" aria-hidden="true">Varlo</div>
    <div class="skyline" role="img" aria-label="Abstract red and black building blocks skyline pattern"></div>
  </section>

  <section class="card" aria-label="Business card">
    <div class="card__rule"></div>
    <h2 class="card__vertical card__name">Varlo Building Pty Ltd</h2>
    <p class="card__vertical card__contact">
      Address : xoxoxoxo, xoxo xoxoxo, xoxoxo - xoxoxo<br>
      Cell : 40404040 E-mail : hello@varlobuilding.com.au
    </p>
    <div class="card__vertical card__mark">Varlo</div>
    <div class="card__vertical card__person">
      <div class="card__person-name">Your Name</div>
      <div class="card__person-role">Designation</div>
    </div>
    <div class="skyline" role="img" aria-label="Abstract red and black building blocks skyline pattern"></div>
  </section>
</body>
</html>
```